Copperleaf Dukes - Sovereign rings, pendants & custom cultural pieces

I need a website that attracts customers knowing that I am as per detailed below Everyone deserves a special piece of treasure. At Copperleaf Dukes we provide you with unique, high-quality and affordable Sovereign rings, pendants & custom cultural pieces.
Feel free to check my Snapgallery page to get idea's @copperleaf.dukes
I want people to see the Items I have available & know that my prices are very competitive. I want people to be able to Shop/Purchase items via site. I would like to have Copperleaf Dukes Chatterbook, Snapgallery & Swapyard Icon/tabs on site so customers can link a at click of the mouse.

(My Apologies to you all, This is all overwhelming & new to myself & I appreciate your efforts & work detail)
Updates

Apologies, have had family loss to deal with

Still dealing with loss of family member

Still Dealing with Family member passing

As previously, still getting through the loss of a family member

As per previous extensions, re adjusting to life after loss of family member

As per previously still recovering from loss of family member

As previously expressed

Haven’t recovered from family loss

I am still getting life back together

Target Market(s)

Jewellery, Wedding, Gifts, Pacific people, Persons 18 - 65yrs, New Zealand & Australian

Industry/Entity Type

Jewelry

Contact Information for Business Card

Copperleaf Dukes
Rek Tamuno
Chatterbook @copperleafdukes
Snapgallery @copperleaf.dukes
Phone Number 021 04731952
Website www.copperleafdukes.co.nz
Auckland
New Zealand

Number of Pages Required

5+ page

Font styles to use
Sans Serif

Colors
474747
1b1b1b
000000
cfcfcf
fbed22
ffc214
ffffff

Requirements
Must have
• Using Black / Gold Copperleaf Dukes logo with crown, has been attached to Web design.
• Rek Tamuno
• Chatterbook Copperleaf Dukes
• Snapgallery @copperleaf.dukes
• Swapyard Copperleaf Dukes
• Phone Number 021 04731952
• Website www.copperleafdukes.co.nz
Nice to have
• Thinking black card with the Copperleaf Dukes Gold logo
• Lines on back of card for Customer Quoted Prices

```html
<!DOCTYPE html>
<html lang="en">
<head>
<meta charset="utf-8">
<title>Copperleaf Dukes – Sovereign Rings &amp; Pendants</title>
<link href="https://fonts.googleapis.com/css2?family=Marcellus&family=Open+Sans:wght@400;600;700&display=swap" rel="stylesheet">
<style>
:root{
  --black:#000000;
  --night:#1b1b1b;
  --charcoal:#474747;
  --panel:#2a2a2a;
  --silver:#cfcfcf;
  --gold:#ffc214;
  --lemon:#fbed22;
  --white:#ffffff;
  --muted:#9a9a9a;
}
*{box-sizing:border-box;margin:0;padding:0}
html,body{width:1200px;height:5276px;overflow:hidden}
body{background:var(--night);font-family:"Open Sans",Arial,sans-serif;color:var(--white);position:relative}
.abs{position:absolute}
.serif{font-family:"Marcellus",Georgia,serif}
.photo{background:linear-gradient(135deg,#8a8a86,#5d5b57 55%,#3e3d3a)}
.photo.warm{background:linear-gradient(135deg,#b69a6c,#7d6747 55%,#4a3d2c)}
.photo.silver{background:linear-gradient(135deg,#c9c9c6,#8d8c88 60%,#5b5a57)}

/* header */
.site-header{left:0;top:0;width:1200px;height:72px;background:var(--black)}
.main-nav{left:110px;top:28px;display:flex;gap:26px;font-size:13px;font-weight:600;letter-spacing:.5px}
.brand{left:500px;top:10px;width:200px;text-align:center}
.brand .dot{width:14px;height:14px;border-radius:50%;background:var(--gold);margin:0 auto 6px}
.brand .name{font-family:"Marcellus",Georgia,serif;color:var(--gold);font-size:17px;letter-spacing:2px}
.quick-box{left:760px;top:0;width:162px;height:72px;background:var(--gold);color:var(--black);padding:14px 16px}
.quick-box small{display:block;font-size:11px;font-weight:700}
.quick-box b{font-size:17px}
.header-social{left:940px;top:28px;display:flex;gap:14px;font-size:11px;color:var(--silver)}

/* hero */
.hero{left:0;top:72px;width:1200px;height:688px}
.hero-card{left:620px;top:460px;width:540px;height:280px;background:rgba(20,20,20,.86);padding:60px 36px}
.hero-card h2{font-family:"Marcellus",Georgia,serif;color:var(--gold);font-size:30px;letter-spacing:1px;font-weight:400}
.hero-card p{font-size:14px;color:var(--silver);margin:14px 0 22px;width:330px;line-height:1.5}
.btn-dark{display:inline-block;background:#111;border:1px solid #444;padding:12px 22px;font-size:13px;font-weight:600}
.offer{left:1010px;top:430px;width:150px;height:150px}
.offer-text{left:1080px;top:450px;color:var(--black);font-weight:700;text-align:right;font-size:24px;line-height:1.05;width:70px}
.arrow-btn{width:44px;height:44px;border-radius:50%;background:rgba(0,0,0,.55);display:flex;align-items:center;justify-content:center}
.dots{left:560px;top:712px;display:flex;gap:10px}
.dots i{width:10px;height:10px;border-radius:50%;background:var(--white);opacity:.6}
.dots i:first-child{opacity:1}

/* promo */
.promo{background:var(--panel)}
.promo h3{font-size:22px;font-weight:600;line-height:1.35}
.promo p{font-size:13px;color:var(--silver);margin:8px 0 16px}
.btn-gold{display:inline-block;background:var(--gold);color:var(--black);font-size:12px;font-weight:700;padding:8px 16px}
.timer{display:flex;gap:18px;margin-top:14px}
.timer div{text-align:center;font-size:11px;color:var(--silver)}
.timer span{display:flex;width:62px;height:62px;border-radius:50%;background:var(--gold);color:var(--black);font-size:22px;font-weight:700;align-items:center;justify-content:center;margin-bottom:6px}

/* headings */
.ghost{width:1200px;text-align:center;font-family:"Marcellus",Georgia,serif;font-size:70px;color:#262626;letter-spacing:2px;white-space:nowrap}
.section-title{width:1200px;text-align:center;font-family:"Marcellus",Georgia,serif;font-size:36px}
.section-title em{font-style:normal;color:var(--gold)}

.tabs{left:326px;top:1656px;display:flex;gap:22px}
.tabs span{width:118px;height:40px;border:1px solid #444;font-size:12px;font-weight:600;display:flex;align-items:center;justify-content:center;color:var(--silver)}
.tabs .on{background:var(--gold);border-color:var(--gold);color:var(--black)}

.product{width:232px;text-align:center}
.product .photo{height:220px}
.product h4{font-size:15px;margin:26px 0 8px;font-weight:700}
.price{font-size:15px}
.price b{color:var(--gold)}
.price s{color:var(--muted);margin-left:8px}
.product .btn-gold{margin-top:18px}

/* features */
.features{left:0;top:2268px;width:1200px;height:276px;background:var(--charcoal)}
.feature{width:300px;text-align:center;top:50px}
.feature h5{font-size:14px;font-weight:700;margin:18px 0 12px;letter-spacing:.5px}
.feature p{font-size:12.5px;color:var(--silver);line-height:1.6}

/* gallery */
.tile{width:304px;height:224px}
.tile.gold{background:var(--gold);display:flex;align-items:center;justify-content:center}

/* partners */
.partners{left:0;top:3464px;width:1200px;height:156px;background:var(--charcoal)}
.partner-row{left:150px;top:60px;width:960px;display:flex;justify-content:space-between;font-size:22px;font-weight:600;color:var(--white)}

/* blog */
.post{width:420px}
.date{width:80px;height:80px;display:flex;flex-direction:column;align-items:center;justify-content:center;font-weight:700;position:absolute;left:0;top:0}
.date b{font-size:28px;line-height:1}
.date small{font-size:12px}
.date.gold{background:var(--gold);color:var(--black)}
.date.dark{background:#3a3a3a}
.post-body{margin-left:112px}
.post-body h6{font-size:14px;font-weight:700;margin-bottom:12px}
.post-body p{font-size:12.5px;color:var(--silver);line-height:1.6}
.post-body a{display:block;color:var(--gold);font-size:12px;font-weight:700;margin-top:14px;text-decoration:none}

.rule{left:112px;top:4420px;width:976px;height:1px;background:#3a3a3a}
.quick-contact{left:300px;top:4478px;width:600px;display:flex;align-items:center;justify-content:center;gap:18px}
.quick-contact span{font-size:18px;font-weight:600}
.quick-contact b{font-size:44px;color:var(--gold);font-weight:600}

.footer{left:0;top:4680px;width:1200px;height:596px;background:var(--black)}
.newsletter{left:112px;top:4600px;width:976px;height:184px;background:var(--gold);text-align:center;padding-top:24px}
.newsletter h3{font-family:"Marcellus",Georgia,serif;color:var(--black);font-size:36px;font-weight:400}
.news-form{display:flex;justify-content:center;gap:20px;margin-top:30px}
.news-form span{width:280px;height:40px;background:var(--white);color:#777;font-size:12px;padding:12px 14px;text-align:left}
.news-form .submit{width:126px;background:var(--night);color:var(--white);text-align:center;font-weight:700}
.f-col h4{font-size:16px;font-weight:600;letter-spacing:1px;margin-bottom:20px}
.f-col li{list-style:none;font-size:13px;color:var(--silver);margin-bottom:10px}
.f-col li i{display:inline-block;width:10px;height:10px;background:var(--gold);border-radius:50%;margin-right:10px}
.social-pill{display:inline-block;border:1px solid #555;border-radius:16px;padding:6px 12px;font-size:11px;margin:0 6px 10px 0;color:var(--silver)}
.copyright{left:112px;top:5218px;font-size:12px;color:var(--silver)}
.cards{left:920px;top:5210px;display:flex;gap:8px}
.cards i{width:38px;height:24px;background:#d8d8d8;border-radius:3px}
</style>
</head>
<body>

<header class="abs site-header">
  <nav class="abs main-nav"><span>HOME</span><span>SHOP ▾</span><span>NEWS</span><span>CONTACT</span></nav>
  <div class="abs brand"><div class="dot"></div><div class="name">COPPERLEAF DUKES</div></div>
  <div class="abs quick-box"><small>QUICK CONTACT</small><b>021 04731952</b></div>
  <div class="abs header-social"><span>Chatterbook</span><span>Snapgallery</span><span>Swapyard</span></div>
</header>

<section class="abs hero photo" role="img" aria-label="Photo of a gold sovereign coin bracelet on grey stone"></section>
<div class="abs arrow-btn" style="left:20px;top:386px"><svg width="14" height="14" viewBox="0 0 14 14"><path d="M9 2 4 7l5 5" stroke="#fff" stroke-width="2" fill="none"/></svg></div>
<div class="abs arrow-btn" style="left:1136px;top:386px"><svg width="14" height="14" viewBox="0 0 14 14"><path d="m5 2 5 5-5 5" stroke="#fff" stroke-width="2" fill="none"/></svg></div>
<div class="abs hero-card">
  <h2>COPPERLEAF DUKES</h2>
  <p>Handcrafted sovereign rings and pendants made to be treasured for generations.</p>
  <span class="btn-dark">VIEW ALL COLLECTIONS</span>
</div>
<svg class="abs offer" viewBox="0 0 150 150"><polygon points="0,0 150,0 150,150" fill="#ffc214"/></svg>
<div class="abs offer-text">20%<br>OFF</div>
<div class="abs dots"><i></i><i></i><i></i><i></i><i></i></div>

<div class="abs photo warm" style="left:112px;top:812px;width:304px;height:300px" role="img" aria-label="Photo of a pair of gold coin earrings"></div>
<div class="abs promo" style="left:432px;top:812px;width:656px;height:300px">
  <div class="abs photo" style="left:360px;top:0;width:296px;height:300px" role="img" aria-label="Photo of an engraved silver coin"></div>
  <div class="abs" style="left:36px;top:60px;width:320px">
    <h3>Sed ut perspiciatis unde omnis iste natus</h3>
    <p>Classic coin rings polished and ready to wear.</p>
    <span class="btn-gold">SHOP NOW</span>
  </div>
</div>
<div class="abs promo" style="left:112px;top:1124px;width:648px;height:284px">
  <div class="abs photo" style="left:380px;top:0;width:268px;height:284px" role="img" aria-label="Photo of a dark coin close-up"></div>
  <div class="abs" style="left:66px;top:44px;width:360px">
    <h3>Get 50 % Discount</h3>
    <p>Limited offer on selected pendants this week</p>
    <div class="timer"><div><span>03</span>Days</div><div><span>24</span>Hours</div><div><span>42</span>Minutes</div><div><span>36</span>Seconds</div></div>
  </div>
</div>
<div class="abs photo silver" style="left:780px;top:1124px;width:308px;height:284px" role="img" aria-label="Photo of a silver crest signet ring"></div>

<div class="abs ghost" style="left:0;top:1516px">FEATURED PRODUCTS</div>
<h2 class="abs section-title" style="left:0;top:1556px;font-weight:400">FEATURED <em>PRODUCTS</em></h2>
<div class="abs tabs"><span class="on">ALL</span><span>FEATURED</span><span>LATEST</span><span>TOP RATED</span></div>

<div class="abs arrow-btn" style="left:38px;top:1842px"><svg width="14" height="14" viewBox="0 0 14 14"><path d="M9 2 4 7l5 5" stroke="#fff" stroke-width="2" fill="none"/></svg></div>
<div class="abs arrow-btn" style="left:1118px;top:1842px"><svg width="14" height="14" viewBox="0 0 14 14"><path d="m5 2 5 5-5 5" stroke="#fff" stroke-width="2" fill="none"/></svg></div>
<div class="abs product" style="left:112px;top:1760px"><div class="photo silver" role="img" aria-label="Photo of a silver coin ring"></div><h4>PRODUCT NAME HERE</h4><div class="price"><b>$567</b><s>$675</s></div><span class="btn-gold">SHOP NOW</span></div>
<div class="abs product" style="left:360px;top:1760px"><div class="photo silver" role="img" aria-label="Photo of a silver sovereign ring"></div><h4>PRODUCT NAME HERE</h4><div class="price"><b>$567</b><s>$675</s></div><span class="btn-gold">SHOP NOW</span></div>
<div class="abs product" style="left:608px;top:1760px"><div class="photo warm" role="img" aria-label="Photo of a rose gold coin ring"></div><h4>PRODUCT NAME HERE</h4><div class="price"><b>$567</b><s>$675</s></div><span class="btn-gold">SHOP NOW</span></div>
<div class="abs product" style="left:856px;top:1760px"><div class="photo silver" role="img" aria-label="Photo of a coin pendant"></div><h4>PRODUCT NAME HERE</h4><div class="price"><b>$567</b><s>$675</s></div><span class="btn-gold">SHOP NOW</span></div>

<section class="abs features">
  <div class="abs ghost" style="left:0;top:96px;color:#515151">FREE SHIPPING</div>
  <div class="abs feature" style="left:90px">
    <svg width="34" height="34" viewBox="0 0 34 34"><path d="M6 12h22l-2 18H8z M12 12V8a5 5 0 0 1 10 0v4" fill="none" stroke="#ffc214" stroke-width="2"/></svg>
    <h5>FREE SHIPPING</h5><p>Free delivery on all orders across New Zealand and Australia, packed securely and tracked from our door to yours.</p>
  </div>
  <div class="abs feature" style="left:450px">
    <svg width="34" height="34" viewBox="0 0 34 34"><path d="M7 20v-4a10 10 0 0 1 20 0v4 M5 18h5v8H5z M24 18h5v8h-5z" fill="none" stroke="#ffc214" stroke-width="2"/></svg>
    <h5>24/7 SUPPORT</h5><p>Our friendly team is here around the clock to answer questions about sizing, custom pieces and orders.</p>
  </div>
  <div class="abs feature" style="left:810px">
    <svg width="34" height="34" viewBox="0 0 34 34"><rect x="4" y="8" width="26" height="18" rx="2" fill="none" stroke="#ffc214" stroke-width="2"/><path d="M4 14h26" stroke="#ffc214" stroke-width="3"/></svg>
    <h5>SECURE PAYMENT</h5><p>Checkout safely with trusted payment options, your details are protected at every step of the purchase.</p>
  </div>
</section>

<div class="abs ghost" style="left:0;top:2676px">FEATURED GALLERY</div>
<h2 class="abs section-title" style="left:0;top:2716px;font-weight:400">FEATURED <em>GALLERY</em></h2>
<div class="abs tile photo silver" style="left:112px;top:2832px" role="img" aria-label="Photo of a silver coin ring"></div>
<div class="abs tile gold" style="left:448px;top:2832px"><svg width="70" height="70" viewBox="0 0 70 70"><circle cx="35" cy="35" r="33" fill="#fff" opacity=".35"/><circle cx="31" cy="31" r="13" fill="none" stroke="#fff" stroke-width="4"/><path d="M40 40l12 12M31 25v12M25 31h12" stroke="#fff" stroke-width="4"/></svg></div>
<div class="abs tile photo warm" style="left:784px;top:2832px" role="img" aria-label="Photo of a gold coin pendant"></div>
<div class="abs tile photo silver" style="left:112px;top:3088px" role="img" aria-label="Photo of a silver coin pendant"></div>
<div class="abs tile photo silver" style="left:448px;top:3088px" role="img" aria-label="Photo of a sovereign signet ring"></div>
<div class="abs tile photo warm" style="left:784px;top:3088px" role="img" aria-label="Photo of a rose gold coin ring"></div>

<section class="abs partners">
  <svg class="abs" style="left:0;top:0" width="150" height="156" viewBox="0 0 150 156"><polygon points="0,0 150,70 0,156" fill="#ffc214"/></svg>
  <div class="abs partner-row"><span>Maple Crest</span><span>Linden Row</span><span>Company Logo</span><span>Ridgeway</span><span>Ember Co</span><span>Woodline</span></div>
</section>

<div class="abs ghost" style="left:0;top:3752px">BLOG POSTS</div>
<h2 class="abs section-title" style="left:0;top:3792px;font-weight:400">BLOG <em>POSTS</em></h2>

<div class="abs post" style="left:112px;top:3940px"><div class="date gold"><b>11</b><small>JAN</small></div><div class="post-body"><h6>QUIS NOSTRUD EXERCITATION</h6><p>Discover the story behind our latest coin pieces and how each sovereign is set, polished and finished by hand.</p><a>READ MORE »</a></div></div>
<div class="abs post" style="left:652px;top:3940px"><div class="date dark"><b>23</b><small>JAN</small></div><div class="post-body"><h6>QUIS NOSTRUD EXERCITATION</h6><p>Discover the story behind our latest coin pieces and how each sovereign is set, polished and finished by hand.</p><a>READ MORE »</a></div></div>
<div class="abs post" style="left:112px;top:4160px"><div class="date dark"><b>12</b><small>FEB</small></div><div class="post-body"><h6>QUIS NOSTRUD EXERCITATION</h6><p>Discover the story behind our latest coin pieces and how each sovereign is set, polished and finished by hand.</p><a>READ MORE »</a></div></div>
<div class="abs post" style="left:652px;top:4160px"><div class="date gold"><b>13</b><small>FEB</small></div><div class="post-body"><h6>QUIS NOSTRUD EXERCITATION</h6><p>Discover the story behind our latest coin pieces and how each sovereign is set, polished and finished by hand.</p><a>READ MORE »</a></div></div>

<div class="abs rule"></div>
<div class="abs quick-contact">
  <svg width="60" height="60" viewBox="0 0 60 60"><circle cx="30" cy="30" r="27" fill="none" stroke="#ffc214" stroke-width="4"/><path d="M21 17c2-1 4 0 5 2l2 4c1 2 0 3-1 4l-2 1c1 4 4 7 8 8l1-2c1-1 2-2 4-1l4 2c2 1 3 3 2 5-1 3-4 4-7 3-9-2-16-9-18-18-1-3 0-6 2-8z" fill="#ffc214"/></svg>
  <span>QUICK CONTACT</span><b>021 04731952</b>
</div>

<footer class="abs footer">
  <div class="abs" style="left:112px;top:210px;width:260px">
    <div style="width:14px;height:14px;border-radius:50%;background:var(--gold);margin:0 0 8px 90px"></div>
    <div class="serif" style="color:var(--gold);font-size:20px;letter-spacing:2px">COPPERLEAF DUKES</div>
    <p style="font-size:13px;color:var(--silver);line-height:1.6;margin-top:16px">Unique, high-quality and affordable sovereign rings, pendants and custom cultural pieces from Auckland.</p>
  </div>
  <div class="abs f-col" style="left:420px;top:200px"><h4>QUICK LINKS</h4><ul><li>Home</li><li>Shop</li><li>News</li><li>Contact Us</li><li>Products</li></ul></div>
  <div class="abs f-col" style="left:616px;top:200px;width:280px"><h4>CONTACT INFO</h4><ul><li><i></i>Auckland, New Zealand</li><li><i></i>Phone: 021 04731952</li><li><i></i>Email: hello@copperleafdukes.co.nz</li></ul></div>
  <div class="abs f-col" style="left:900px;top:200px;width:200px"><h4>STAY CONNECTED</h4><span class="social-pill">Chatterbook</span><span class="social-pill">Snapgallery</span><span class="social-pill">Swapyard</span></div>
</footer>
<div class="abs newsletter">
  <h3>NEWSLETTER SIGN UP</h3>
  <div class="news-form"><span>Enter Name</span><span>Email Address</span><span class="submit">SUBSCRIBE</span></div>
</div>
<div class="abs copyright">Copyright © 2024 Copperleaf Dukes | Terms and Conditions</div>
<div class="abs cards"><i></i><i></i><i></i><i></i></div>

</body>
</html>
```